Driver License Monitoring Application Marketing Website

We need a new web design for our web application. The product is called "PermitPulseNow." We provide a driver license monitoring service to companies and local government bodies with driver fleets. Our current website is available at www.permitpulsenow.example.

I prefer a clean, single-page design with good SEO. Attached are some PDFs with data about the project.

Target Market(s)

Companies with driver fleets, local government.

Industry/Entity Type

Government

Coding

Coded - Design and coding required

Number of Pages Required

1 page

Colors
000000

Requirements
Must have
• Content from current www.permitpulsenow.example and attached PDFs.
Nice to have
• Prefer a simple Bootstrap or similar design for easy editing.
• Room for a simple video explanation of how the product works (we don't have an actual video yet)

```html
<!DOCTYPE html>
<html lang="en">
<head>
<meta charset="utf-8">
<title>PermitPulseNow – Florida Driver License Monitoring</title>
<link rel="stylesheet" href="https://fonts.googleapis.com/css2?family=Cinzel:wght@400;700&family=Lato:wght@400;700&display=swap">
<style>
:root{
  --red:#b3131b;
  --black:#000;
  --ink:#1a1a1a;
  --text:#333;
  --muted:#666;
  --rule:#e2e2e2;
  --hero-bg:#e6e6e6;
  --band:#1c1c1c;
  --footer:#202020;
  --footer-bottom:#2b2b2b;
  --footer-text:#9a9a9a;
}
*{margin:0;padding:0;box-sizing:border-box}
html,body{width:838px;height:1200px;overflow:hidden;background:#fff}
body{font-family:'Lato',sans-serif;color:var(--text);position:relative}
.abs{position:absolute}
.red{color:var(--red)}

/* header */
.site-header{position:absolute;top:0;left:0;width:838px;height:78px;background:#fff}
.brand{left:92px;top:28px;font-family:'Cinzel',serif;font-weight:700;font-size:20px;color:var(--black);letter-spacing:.5px}
.main-nav{left:359px;top:37px;display:flex;gap:14px;font-size:9.5px;color:var(--ink);text-transform:uppercase}
.main-nav .active{color:var(--red)}
.btn-login{left:643px;top:28px;width:71px;height:25px;background:var(--black);color:#fff;font-size:9.5px;display:flex;align-items:center;justify-content:center;gap:6px}
.btn-search{left:720px;top:28px;width:26px;height:25px;background:var(--black);display:flex;align-items:center;justify-content:center}

/* hero */
.hero{position:absolute;top:78px;left:0;width:838px;height:259px;background:radial-gradient(ellipse at 50% 45%,#f2f2f2,#dcdcdc)}
.hero-media{left:92px;top:32px;width:378px;height:200px;background:linear-gradient(135deg,#7fc94a,#4f9a2a 60%,#6e6e6e);border-radius:6px}
.hero-arrow{top:113px;width:20px;height:36px;background:#fff;box-shadow:0 1px 3px rgba(0,0,0,.2);display:flex;align-items:center;justify-content:center}
.hero-arrow.prev{left:46px;border-radius:18px 0 0 18px}
.hero-arrow.next{left:768px;border-radius:18px 0 0 18px;width:20px}
.hero-title{left:478px;top:67px;width:276px;text-align:center;font-family:'Cinzel',serif;font-size:20px;line-height:24px;color:var(--black);letter-spacing:.5px}
.hero-copy{left:478px;top:125px;width:276px;text-align:center;font-size:10.5px;line-height:15px;color:#444}
.hero-copy b{color:var(--red)}
.btn-more{left:573px;top:181px;width:87px;height:21px;background:var(--black);color:#fff;font-family:'Cinzel',serif;font-size:10.5px;display:flex;align-items:center;justify-content:center}

/* section headings */
.section-title{font-size:16px;font-weight:700;color:var(--black);text-transform:uppercase;padding-bottom:8px;border-bottom:1px solid var(--rule);position:absolute}
.section-title::after{content:"";position:absolute;left:14px;bottom:-5px;width:8px;height:8px;background:#fff;border-right:1px solid var(--rule);border-bottom:1px solid var(--rule);transform:rotate(45deg)}
.section-title span{color:var(--red)}

/* features */
.features{position:absolute;top:337px;left:0;width:838px;height:239px}
.feature-list{left:92px;top:63px;height:112px;border-left:1px solid #ccc;list-style:none}
.feature-list li{position:relative;font-size:17px;color:var(--ink);padding-left:41px;height:30px;line-height:22px}
.feature-list li::before{content:"";position:absolute;left:0;top:11px;width:22px;border-top:1px solid #ccc}
.feature-list li::after{content:"";position:absolute;left:21px;top:9px;width:4px;height:4px;border-radius:50%;background:#bbb}
.feature-list li.current{color:var(--red)}
.video{left:492px;top:61px;width:254px;height:150px;background:linear-gradient(120deg,#d6dde6,#9fb1c6 55%,#e8ecf0)}
.video-play{left:110px;top:52px;width:34px;height:34px;border-radius:50%;background:#fff;display:flex;align-items:center;justify-content:center}
.video-bar{left:0;bottom:0;width:254px;height:16px;background:#0d0d0d;color:#fff;font-size:7px;display:flex;align-items:center;padding:0 6px;gap:6px}
.video-track{flex:1;height:4px;background:#555;border-radius:2px;position:relative}
.video-track i{position:absolute;left:0;top:0;width:12%;height:4px;background:#3d7fd6;border-radius:2px}

/* services band */
.services{position:absolute;top:576px;left:0;width:838px;height:183px;background:radial-gradient(circle at 20% 50%,#2e2e2e,var(--band) 60%)}
.service{top:42px;width:160px;text-align:center;color:#fff}
.service .ring{width:68px;height:68px;margin:0 auto;border-radius:50%;border:2px solid #fff;display:flex;align-items:center;justify-content:center}
.service .ring.filled{background:var(--red)}
.service h3{font-size:13px;font-weight:700;margin-top:15px}
.service p{font-size:10px;margin-top:4px;color:#ddd}

/* alerts & benefits */
.details{position:absolute;top:759px;left:0;width:838px;height:258px}
.tick-list{list-style:none;font-size:10.5px;color:#333}
.tick-list li{position:relative;padding-left:20px;height:16.8px;line-height:14px}
.tick-list li svg{position:absolute;left:1px;top:1px}
.tick-list .sub{padding-left:0;height:auto}
.tick-list .sub div{padding-left:11px;height:14.9px;line-height:14px}
.truck-photo{left:310px;top:66px;width:196px;height:163px;border:2px solid var(--black);background:linear-gradient(180deg,#bcd8f0 0%,#9fb9cf 35%,#a9222c 55%,#6b6b6b 80%,#8b8b8b)}

/* footer */
.site-footer{position:absolute;top:1017px;left:0;width:838px;height:115px;background:var(--footer);color:var(--footer-text)}
.footer-brand{left:92px;top:23px;font-family:'Cinzel',serif;font-weight:700;font-size:15px;color:#fff;letter-spacing:.5px}
.footer-address{left:92px;top:50px;font-size:9.5px;line-height:17px}
.footer-divider{top:24px;width:1px;height:64px;background:#3a3a3a}
.newsletter h4,.contact h4{font-size:12px;font-weight:400;color:#fff;text-transform:uppercase}
.newsletter{left:327px;top:21px;width:197px;text-align:center}
.newsletter-field{margin-top:20px;height:29px;border:1px solid #3d3d3d;display:flex;align-items:center;justify-content:space-between;padding:0 10px;font-size:9.5px;color:#8a8a8a;text-align:left}
.contact{right:92px;top:21px;text-align:right;font-size:9.5px;line-height:17px}
.contact h4{margin-bottom:6px}
.contact b{color:#fff;font-weight:700}
.footer-bottom{position:absolute;top:1132px;left:0;width:838px;height:68px;background:var(--footer-bottom);text-align:center}
.social{position:absolute;top:16px;left:375px;display:flex;gap:7px}
.social i{width:16px;height:16px;border-radius:50%;background:#5a5a5a;display:block}
.copyright{position:absolute;top:44px;width:100%;font-size:9px;color:var(--footer-text)}
</style>
</head>
<body>

<header class="site-header">
  <div class="abs brand">PermitPulseNow</div>
  <nav class="abs main-nav">
    <span class="active">Home</span><span>License-Monitoring</span><span>About Us</span><span>Contact Us</span>
  </nav>
  <div class="abs btn-login">
    <svg width="9" height="9" viewBox="0 0 10 10"><circle cx="5" cy="3" r="2.3" fill="#fff"/><path d="M0.5 10c0-3 2-4.5 4.5-4.5S9.5 7 9.5 10z" fill="#fff"/></svg>LOGIN
  </div>
  <div class="abs btn-search">
    <svg width="16" height="16" viewBox="0 0 16 16"><circle cx="6.5" cy="6.5" r="4.8" fill="none" stroke="#fff" stroke-width="1.8"/><line x1="10" y1="10" x2="14.5" y2="14.5" stroke="#fff" stroke-width="2"/></svg>
  </div>
</header>

<section class="hero">
  <div class="abs hero-arrow prev"><svg width="8" height="10" viewBox="0 0 8 10"><path d="M6 1 2 5l4 4" fill="none" stroke="#111" stroke-width="2"/></svg></div>
  <div class="abs hero-media" role="img" aria-label="Green refuse collection truck"></div>
  <h1 class="abs hero-title">Florida <span class="red">Driver License</span><br>Monitoring</h1>
  <p class="abs hero-copy">Monitor Your Fleet <b>Electronically</b>. Get Alerts By <b>Email</b> And <b>Online</b>. Never Let Another Unlicensed Or Unauthorized Driver Behind The Wheel.</p>
  <div class="abs btn-more">Read More</div>
  <div class="abs hero-arrow next"><svg width="8" height="10" viewBox="0 0 8 10"><path d="M2 1l4 4-4 4" fill="none" stroke="#111" stroke-width="2"/></svg></div>
</section>

<section class="features">
  <h2 class="section-title" style="left:92px;top:23px;width:368px">Monitor Your <span>Whole Feet Online</span></h2>
  <ul class="abs feature-list">
    <li class="current">Secure</li>
    <li>Available 24 hours a day</li>
    <li>&nbsp;Desktop or Mobie</li>
  </ul>
  <h2 class="section-title" style="left:492px;top:23px;width:254px">Our <span>Video</span></h2>
  <div class="abs video" role="img" aria-label="Video preview of a smiling businessman in an office">
    <div class="abs video-play"><svg width="12" height="14" viewBox="0 0 12 14"><path d="M1 0l11 7-11 7z" fill="#111"/></svg></div>
    <div class="abs video-bar">
      <svg width="6" height="7" viewBox="0 0 6 7"><path d="M0 0l6 3.5L0 7z" fill="#fff"/></svg>
      <span>04:59</span><div class="video-track"><i></i></div><span>10:35</span>
      <svg width="8" height="7" viewBox="0 0 8 7"><path d="M0 2h2l2-2v7L2 5H0z" fill="#fff"/><path d="M5.5 1.5a3 3 0 0 1 0 4" stroke="#fff" fill="none"/></svg>
      <svg width="7" height="7" viewBox="0 0 7 7"><path d="M0 7 7 0M4 0h3v3M0 4v3h3" stroke="#fff" fill="none"/></svg>
    </div>
  </div>
</section>

<section class="services">
  <div class="abs service" style="left:93px">
    <div class="ring filled"><svg width="30" height="32" viewBox="0 0 30 32"><path d="M15 2a10 10 0 0 0-6 18v4h12v-4a10 10 0 0 0-6-18z" fill="#fff"/><rect x="10" y="26" width="10" height="2" fill="#fff"/><rect x="11" y="29" width="8" height="2" fill="#fff"/></svg></div>
    <h3>What We Do</h3><p>License Monitoring</p>
  </div>
  <div class="abs service" style="left:256px">
    <div class="ring"><svg width="32" height="32" viewBox="0 0 32 32" fill="none" stroke="#fff" stroke-width="1.6"><path d="M4 30V14l8-4v20M12 30V6l10-4v28M22 30V12l6 3v15M2 30h28"/><path d="M15 9h4M15 13h4M15 17h4M15 21h4M7 17h2M7 21h2M24 18h2M24 22h2"/></svg></div>
    <h3>Commercial</h3><p>Private Sector</p>
  </div>
  <div class="abs service" style="left:419px">
    <div class="ring"><svg width="32" height="30" viewBox="0 0 32 30" fill="#fff"><path d="M16 1 2 8h28z"/><rect x="3" y="9" width="26" height="2"/><rect x="5" y="12" width="3" height="12"/><rect x="11" y="12" width="3" height="12"/><rect x="18" y="12" width="3" height="12"/><rect x="24" y="12" width="3" height="12"/><rect x="3" y="25" width="26" height="2"/><rect x="1" y="28" width="30" height="2"/></svg></div>
    <h3>Government</h3><p>Public Sector</p>
  </div>
  <div class="abs service" style="left:582px">
    <div class="ring"><svg width="36" height="30" viewBox="0 0 36 30" fill="#fff"><circle cx="14" cy="8" r="7"/><path d="M0 28c0-8 6-12 14-12s14 4 14 12z"/><circle cx="26" cy="15" r="5" stroke="#1c1c1c" stroke-width="1.5"/><path d="M17 30c0-6 4-9 9-9s9 3 9 9z" stroke="#1c1c1c" stroke-width="1.5"/></svg></div>
    <h3>About Us</h3><p>Florida Law Authorities</p>
  </div>
</section>

<section class="details">
  <h2 class="section-title" style="left:91px;top:23px;width:212px">Get Instant <span>Email Alerts</span></h2>
  <ul class="abs tick-list" style="left:92px;top:66px">
    <li><svg width="12" height="11" viewBox="0 0 12 11"><path d="M1 6l3.5 4L11 1" fill="none" stroke="#b3131b" stroke-width="2.4"/></svg>Suspensions For Child Support</li>
    <li><svg width="12" height="11" viewBox="0 0 12 11"><path d="M1 6l3.5 4L11 1" fill="none" stroke="#b3131b" stroke-width="2.4"/></svg>Suspensions For Unpaid Fines</li>
    <li><svg width="12" height="11" viewBox="0 0 12 11"><path d="M1 6l3.5 4L11 1" fill="none" stroke="#b3131b" stroke-width="2.4"/></svg>Suspensions For Court Obligations</li>
    <li><svg width="12" height="11" viewBox="0 0 12 11"><path d="M1 6l3.5 4L11 1" fill="none" stroke="#b3131b" stroke-width="2.4"/></svg>Revocations For Accidents</li>
    <li><svg width="12" height="11" viewBox="0 0 12 11"><path d="M1 6l3.5 4L11 1" fill="none" stroke="#b3131b" stroke-width="2.4"/></svg>Revocations For Convictions</li>
    <li><svg width="12" height="11" viewBox="0 0 12 11"><path d="M1 6l3.5 4L11 1" fill="none" stroke="#b3131b" stroke-width="2.4"/></svg>Commercial Vehicle Disqualifications</li>
    <li><svg width="12" height="11" viewBox="0 0 12 11"><path d="M1 6l3.5 4L11 1" fill="none" stroke="#b3131b" stroke-width="2.4"/></svg>Medical Certificate Expirations</li>
    <li><svg width="12" height="11" viewBox="0 0 12 11"><path d="M1 6l3.5 4L11 1" fill="none" stroke="#b3131b" stroke-width="2.4"/></svg>License Expirations</li>
    <li><svg width="12" height="11" viewBox="0 0 12 11"><path d="M1 6l3.5 4L11 1" fill="none" stroke="#b3131b" stroke-width="2.4"/></svg>License Cancellations</li>
    <li><svg width="12" height="11" viewBox="0 0 12 11"><path d="M1 6l3.5 4L11 1" fill="none" stroke="#b3131b" stroke-width="2.4"/></svg>All Other License Sanctions</li>
  </ul>
  <div class="abs truck-photo" role="img" aria-label="Red semi truck on a coastal highway"></div>
  <h2 class="section-title" style="left:535px;top:23px;width:211px">Our <span>Benefits</span></h2>
  <ul class="abs tick-list" style="left:534px;top:66px">
    <li><svg width="12" height="11" viewBox="0 0 12 11"><path d="M1 6l3.5 4L11 1" fill="none" stroke="#b3131b" stroke-width="2.4"/></svg>Recive license Alerts Immediately by Email</li>
    <li class="sub" style="padding-left:17px">
      <div>- Suspensions</div><div>- Revocations</div><div>- Expirations</div><div>- Cancellations</div><div>- Disqualifications</div><div>- Other Driver Sanctions</div>
    </li>
    <li><svg width="12" height="11" viewBox="0 0 12 11"><path d="M1 6l3.5 4L11 1" fill="none" stroke="#b3131b" stroke-width="2.4"/></svg>Improve Public Safety</li>
    <li><svg width="12" height="11" viewBox="0 0 12 11"><path d="M1 6l3.5 4L11 1" fill="none" stroke="#b3131b" stroke-width="2.4"/></svg>Encourage Responsible Employee Behavior</li>
    <li><svg width="12" height="11" viewBox="0 0 12 11"><path d="M1 6l3.5 4L11 1" fill="none" stroke="#b3131b" stroke-width="2.4"/></svg>Reduce Insurance Premiums</li>
    <li><svg width="12" height="11" viewBox="0 0 12 11"><path d="M1 6l3.5 4L11 1" fill="none" stroke="#b3131b" stroke-width="2.4"/></svg>Increase Productivity</li>
  </ul>
</section>

<footer class="site-footer">
  <div class="abs footer-brand">PermitPulseNow</div>
  <address class="abs footer-address" style="font-style:normal">4410 Harbor Crest Ave., Ste 210<br>Bayview, FL 33999</address>
  <div class="abs footer-divider" style="left:287px"></div>
  <div class="abs newsletter">
    <h4>Sign Up For Newsletter</h4>
    <div class="newsletter-field"><span>Enter your email here</span><svg width="8" height="6" viewBox="0 0 8 6"><path d="M0 3h7M4.5 0.5 7 3 4.5 5.5" fill="none" stroke="#bbb"/></svg></div>
  </div>
  <div class="abs footer-divider" style="left:564px"></div>
  <div class="abs contact">
    <h4>Contact Us</h4>
    <div><b>M</b>: 1.555.010.2468</div>
    <div><b>F</b>: (555) 010-7731</div>
    <div><b>E</b>: contact@permitpulsenow.example</div>
  </div>
</footer>
<div class="footer-bottom">
  <div class="social"><i></i><i></i><i></i><i></i></div>
  <p class="copyright">© 2015 PermitPulseNow. All Rights Reserved.</p>
</div>

</body>
</html>
```